Stationery Design Project - KTRV-PRIME

Presentation Folder
Size: A4
Notepad
Size: 250mm x 140mm
With Compliments Slip
Size: DL
210mm x 99mm
Letterhead
Size: A4 - 210mm x 297mm
Business Cards
Size: 90mm x 55mm

Company is called "KTRV-PRIME"
website: www.ktrvprime.com.au (under construction)

Offices: *Perth *Brisbane *Seoul *Hong Kong

If you need any further information please let me know!

Cheers

Neil

```html
<!DOCTYPE html>
<html lang="en">
<head>
<meta charset="utf-8">
<title>KTRV-PRIME Stationery – Notepad and Compliments Slip</title>
<link href="https://fonts.googleapis.com/css2?family=Tinos:wght@400;700&family=Lobster&family=Open+Sans:wght@400&display=swap" rel="stylesheet">
<style>
  :root {
    --backdrop: #e9e7e4;
    --paper: #ffffff;
    --ink: #222222;
    --ink-soft: #555555;
    --brand-blue: #2b8cc4;
    --brand-navy: #2b3a8f;
    --brand-cyan: #29b6e8;
    --brand-grey: #8e949a;
    --label: #5a5a5a;
  }
  * { margin: 0; padding: 0; box-sizing: border-box; }
  html, body { width: 1200px; height: 508px; overflow: hidden; }
  body {
    position: relative;
    background: var(--backdrop);
    font-family: "Tinos", "Times New Roman", serif;
    color: var(--ink);
  }

  .sheet { position: absolute; background: var(--paper); }

  .brand { position: absolute; display: flex; align-items: center; gap: 12px; }
  .brand-square { width: 14px; height: 14px; background: var(--brand-blue); }
  .brand-name {
    font-family: "Tinos", "Times New Roman", serif;
    font-weight: 400; color: var(--brand-blue); letter-spacing: 2px;
  }

  /* Notepad */
  .notepad { left: 31px; top: 26px; width: 494px; height: 413px; }
  .notepad .brand { left: 28px; top: 58px; }
  .notepad .brand-name { font-size: 34px; }
  .notepad-address { position: absolute; left: 148px; top: 134px; font-size: 13px; }
  .notepad-web {
    position: absolute; left: 22px; top: 388px;
    font-size: 14px; letter-spacing: 1.4px; color: var(--ink);
  }

  /* Compliments slip */
  .slip { left: 550px; top: 79px; width: 621px; height: 293px; }
  .slip .brand { left: 22px; top: 52px; }
  .slip .brand-name { font-size: 32px; }
  .slip-greeting {
    position: absolute; right: 21px; top: 36px; text-align: right;
    font-family: "Lobster", cursive; font-size: 30px; line-height: 31px;
    color: var(--brand-blue);
  }
  .slip-edge-left {
    position: absolute; left: 0; top: 164px; width: 9px; height: 108px;
    border-radius: 0 6px 6px 0;
    background: linear-gradient(to bottom, var(--brand-navy), var(--brand-cyan) 45%, var(--brand-navy));
  }
  .slip-edge-right {
    position: absolute; right: 0; top: 220px; width: 9px; height: 51px;
    border-radius: 6px 0 0 6px;
    background: linear-gradient(to right, #d8dadc, var(--brand-grey));
  }
  .contact-list { position: absolute; left: 20px; top: 170px; list-style: none; font-size: 13px; }
  .contact-list li { display: flex; align-items: center; gap: 6px; height: 18px; }
  .contact-list svg { width: 11px; height: 11px; fill: var(--brand-navy); }
  .slip-address { position: absolute; left: 20px; top: 251px; font-size: 13px; }
  .signatory { position: absolute; right: 14px; top: 226px; text-align: right; }
  .signatory-name { font-size: 17px; font-weight: 700; color: var(--brand-blue); line-height: 19px; }
  .signatory-role { font-size: 10px; color: var(--ink-soft); }

  .item-label {
    position: absolute; font-family: "Open Sans", Arial, sans-serif;
    color: var(--label); text-align: center;
  }
  .label-notepad { left: 185px; top: 450px; width: 200px; font-size: 33px; }
  .label-slip { left: 680px; top: 380px; width: 360px; font-size: 42px; }
</style>
</head>
<body>

<section class="sheet notepad" aria-label="Notepad">
  <div class="brand"><span class="brand-square"></span><span class="brand-name">KTRV-PRIME</span></div>
  <p class="notepad-address">00, Complex Name, City, State 0004</p>
  <p class="notepad-web">www.ktrvprime.com.au</p>
</section>
<p class="item-label label-notepad">Notepad</p>

<section class="sheet slip" aria-label="Compliments slip">
  <div class="brand"><span class="brand-square"></span><span class="brand-name">KTRV-PRIME</span></div>
  <p class="slip-greeting">With Best<br>Compliments</p>
  <div class="slip-edge-left"></div>
  <div class="slip-edge-right"></div>
  <ul class="contact-list">
    <li><svg viewBox="0 0 12 12"><path d="M3 1l2 3-1.2 1.2a7 7 0 0 0 3 3L8 7l3 2-1.5 2C5 11 1 7 1 2.5z"/></svg>123-456-7890</li>
    <li><svg viewBox="0 0 12 12"><path d="M3.5 0h5a1 1 0 0 1 1 1v10a1 1 0 0 1-1 1h-5a1 1 0 0 1-1-1V1a1 1 0 0 1 1-1zm.5 1.5v7h4v-7z"/></svg>123-456-7890</li>
    <li><svg viewBox="0 0 12 12"><path d="M1 3h10v7H1zm1 1l4 3 4-3z"/></svg>info@ktrvprime.com.au</li>
    <li><svg viewBox="0 0 12 12"><circle cx="6" cy="6" r="5"/><path d="M1 6h10M6 1v10" stroke="#fff" stroke-width="0.8"/></svg>www.ktrvprime.com.au</li>
  </ul>
  <p class="slip-address">00, Complex Name, City, State 0004</p>
  <div class="signatory">
    <p class="signatory-name">Your Name</p>
    <p class="signatory-role">Designation</p>
  </div>
</section>
<p class="item-label label-slip">Compliments Slip</p>

</body>
</html>
```